New Managed IT company needs a business card

We are an IT management and support company that needs a business card design. I have a logo that I'll provide. Blues and blacks match the logo, but i'm open to anything. I want the card to help people take us seriously, but still have some energy and fun in it. The card should communicate stability and a solid company.

Target Market(s)

Target market includes Owners and Presidents at small businesses of 20 - 100 employees in the Pittsburgh PA area.

Industry/Entity Type

Information Technology

Contact Information for Business Card

i am open to other designs, but i imagine having only the logo on one side and then the logo plus all contact details on the other side.

Requirements
Must have
• Our logo
• Company name is optional if the logo makes it obvious
• A name - Cole Perrin
• A title - President
• A phone number - 724-XXX-XXXX
• A mobile phone number - 724-615-2748
• An email address - cperrin@techvaultgrid.com
• a website - techvaultgrid.com or www.techvaultgrid.com
Nice to have
• some people tell me the logo feels like a superhero theme, some fun with that idea might be good. I'm open to ideas.
Should not have
• stock photos of people or computers - especially old looking stuff.

```html
<!DOCTYPE html>
<html lang="en">
<head>
<meta charset="utf-8">
<title>TechVault Grid – Business Card</title>
<link href="https://fonts.googleapis.com/css2?family=Montserrat:wght@700&family=Roboto+Slab:wght@400&display=swap" rel="stylesheet">
<style>
  :root {
    --backdrop: #e9e6e1;
    --card-white: #ffffff;
    --card-black: #1e1e20;
    --brand-blue: #0aa0e6;
    --ink-dark: #1c1c1e;
    --ink-light: #ffffff;
  }
  * { margin: 0; padding: 0; box-sizing: border-box; }
  html, body {
    width: 1200px; height: 913px; overflow: hidden;
    background: var(--backdrop);
  }
  .canvas { position: relative; width: 1200px; height: 913px; }

  .card {
    position: absolute;
    width: 560px; height: 320px;
    border-radius: 4px;
    overflow: hidden;
    box-shadow: 0 10px 28px rgba(0,0,0,0.22);
  }

  /* Front */
  .card-front { left: 80px; top: 120px; background: var(--card-white); }
  .brand-lockup {
    position: absolute; left: 50%; top: 50%;
    transform: translate(-50%, -50%);
    display: flex; align-items: center; gap: 16px;
    white-space: nowrap;
  }
  .brand-dot {
    flex: 0 0 auto;
    width: 54px; height: 54px; border-radius: 50%;
    background: var(--brand-blue);
  }
  .brand-name {
    font-family: "Montserrat", sans-serif; font-weight: 700;
    font-size: 30px; letter-spacing: 2px; text-transform: uppercase;
    color: var(--ink-dark);
  }

  /* Back */
  .card-back { left: 560px; top: 470px; background: var(--card-black); }
  .accent-field {
    position: absolute; right: 0; top: 0;
    width: 390px; height: 130px;
    background: linear-gradient(200deg, var(--brand-blue) 0%, rgba(10,160,230,0.35) 45%, rgba(30,30,32,0) 85%);
  }
  .holder { position: absolute; left: 36px; top: 120px; font-family: "Roboto Slab", serif; }
  .holder-name {
    font-size: 30px; color: var(--brand-blue);
    text-transform: uppercase; line-height: 1;
  }
  .holder-title { font-size: 16px; color: var(--ink-light); margin-top: 6px; }

  .contact-list {
    position: absolute; left: 36px; top: 186px;
    list-style: none; font-family: "Roboto Slab", serif;
    font-size: 14px; color: var(--ink-light);
  }
  .contact-list li { display: flex; align-items: center; gap: 10px; height: 22px; white-space: nowrap; }
  .contact-icon {
    flex: 0 0 auto;
    width: 16px; height: 16px; border-radius: 50%;
    background: var(--brand-blue);
    display: flex; align-items: center; justify-content: center;
  }
  .contact-icon svg { width: 10px; height: 10px; }

  .web-band {
    position: absolute; left: 0; bottom: 22px;
    width: 420px; height: 38px;
    background: var(--brand-blue);
    border-radius: 0 8px 8px 0;
    display: flex; align-items: center; gap: 12px; padding-left: 36px;
    font-family: "Roboto Slab", serif; font-size: 18px; color: var(--ink-light);
    white-space: nowrap;
  }
  .web-band svg { width: 20px; height: 20px; flex: 0 0 auto; }
</style>
</head>
<body>
<main class="canvas">

  <section class="card card-front" aria-label="Card front">
    <div class="brand-lockup">
      <span class="brand-dot"></span>
      <span class="brand-name">TechVault Grid</span>
    </div>
  </section>

  <section class="card card-back" aria-label="Card back">
    <div class="accent-field" role="img" aria-label="Decorative blue swoosh artwork"></div>

    <div class="holder">
      <p class="holder-name">Cole Perrin</p>
      <p class="holder-title">President</p>
    </div>

    <ul class="contact-list">
      <li>
        <span class="contact-icon"><svg viewBox="0 0 10 10"><path fill="#1e1e20" d="M2 1 L4 1 L4.5 3 L3.5 4 Q4.5 6 6 6.5 L7 5.5 L9 6 L9 8 Q5 9 2 6 Q1 4 2 1 Z"/></svg></span>
        724-XXX-XXXX
      </li>
      <li>
        <span class="contact-icon"><svg viewBox="0 0 10 10"><rect x="2.8" y="0.8" width="4.4" height="8.4" rx="0.8" fill="none" stroke="#1e1e20" stroke-width="1.1"/></svg></span>
        724-615-2748
      </li>
      <li>
        <span class="contact-icon"><svg viewBox="0 0 10 10"><rect x="1" y="2.5" width="8" height="5.5" fill="#1e1e20"/><path d="M1 2.5 L5 5.5 L9 2.5" fill="none" stroke="#0aa0e6" stroke-width="0.9"/></svg></span>
        cperrin@techvaultgrid.com
      </li>
    </ul>

    <div class="web-band">
      <svg viewBox="0 0 20 20" aria-hidden="true">
        <circle cx="10" cy="10" r="8.5" fill="none" stroke="#ffffff" stroke-width="1.6"/>
        <ellipse cx="10" cy="10" rx="3.6" ry="8.5" fill="none" stroke="#ffffff" stroke-width="1.2"/>
        <line x1="1.5" y1="10" x2="18.5" y2="10" stroke="#ffffff" stroke-width="1.2"/>
      </svg>
      www.techvaultgrid.com
    </div>
  </section>

</main>
</body>
</html>
```